Home Baker of cakes, muffins, cookies and pastries.

I am looking for business cards for my home baking business called " Zippy Pom-Pom Bakes " - I want them to be super cute and girly, yet simple and modern at the same time. Pastel colours is what I envision with the main colour being baby pink.

```html
<!DOCTYPE html>
<html lang="en">
<head>
<meta charset="utf-8">
<title>Zippy Pom-Pom Bakes – Business Cards</title>
<link rel="stylesheet" href="https://fonts.googleapis.com/css2?family=Dancing+Script:wght@500&family=Sniglet&family=Varela+Round&display=swap">
<style>
  :root {
    --page: #f3efea;
    --baby-pink: #f0908f;
    --pattern-pink-soft: #f7cfce;
    --pattern-pink-mid: #f2b2b1;
    --mint: #8fcf95;
    --mint-light: #b4e0b7;
    --mint-deep: #86c98c;
    --white: #ffffff;
  }
  * { margin: 0; padding: 0; box-sizing: border-box; }
  html, body {
    width: 900px; height: 1200px; overflow: hidden;
    background: var(--page);
  }
  .canvas { position: relative; width: 900px; height: 1200px; }

  .card {
    position: absolute; left: 88px; width: 734px; height: 430px;
    border-radius: 22px; overflow: hidden;
    box-shadow: 0 6px 16px rgba(0,0,0,0.18);
  }
  .card--front { top: 125px; background: var(--mint); }
  .card--back  { top: 640px; background: var(--white); }

  /* Front */
  .pattern-strip {
    position: absolute; top: 0; width: 112px; height: 100%;
    background:
      radial-gradient(circle at 30% 20%, var(--mint-light) 0, transparent 45%),
      radial-gradient(circle at 70% 55%, var(--mint-light) 0, transparent 40%),
      radial-gradient(circle at 35% 88%, var(--mint-light) 0, transparent 40%),
      linear-gradient(180deg, var(--mint-deep), var(--mint));
  }
  .pattern-strip--left { left: 0; }
  .pattern-strip--right { right: 0; width: 117px; }
  .front-panel {
    position: absolute; left: 112px; top: 0; width: 505px; height: 100%;
    background: var(--baby-pink); color: var(--white); text-align: center;
  }
  .brand-dot {
    width: 96px; height: 96px; border-radius: 50%;
    border: 3px solid var(--white);
  }
  .front-panel .brand-dot { margin: 52px auto 0; }
  .brand-name {
    font-family: "Dancing Script", cursive;
    font-weight: 500; font-size: 46px; line-height: 1;
  }
  .front-panel .brand-name { margin-top: 28px; }
  .tagline {
    font-family: "Sniglet", sans-serif;
    font-size: 21px; letter-spacing: 0.4px; line-height: 1.1;
  }
  .front-panel .tagline { margin-top: 6px; }
  .person-name {
    font-family: "Dancing Script", cursive;
    font-weight: 500; font-size: 44px; line-height: 1; margin-top: 26px;
  }
  .contact {
    font-family: "Varela Round", sans-serif;
    font-size: 16px; letter-spacing: 0.6px; line-height: 25px; margin-top: 8px;
  }

  /* Back */
  .pattern-band {
    position: absolute; left: 0; width: 100%; height: 128px;
    background:
      radial-gradient(circle at 15% 40%, var(--pattern-pink-mid) 0, transparent 30%),
      radial-gradient(circle at 50% 60%, var(--pattern-pink-mid) 0, transparent 30%),
      radial-gradient(circle at 85% 40%, var(--pattern-pink-mid) 0, transparent 30%),
      var(--pattern-pink-soft);
  }
  .pattern-band--top { top: 0; }
  .pattern-band--bottom { bottom: 0; }
  .back-band {
    position: absolute; left: 0; top: 128px; width: 100%; height: 174px;
    background: var(--baby-pink); color: var(--white);
    display: flex; align-items: center; justify-content: center; gap: 10px;
  }
  .back-brand { text-align: left; }
  .back-band .brand-name { font-size: 52px; padding-left: 4px; }
  .back-band .tagline { font-size: 23px; margin-top: 8px; }
  .back-band .brand-dot { width: 100px; height: 100px; flex: none; }
</style>
</head>
<body>
<main class="canvas">

  <section class="card card--front">
    <div class="pattern-strip pattern-strip--left" role="img" aria-label="White bakery icon pattern of cupcakes, cakes, donuts and pastries on mint green"></div>
    <div class="front-panel">
      <div class="brand-dot"></div>
      <h1 class="brand-name">Zippy Pom-Pom Bakes</h1>
      <p class="tagline">cakes, muffins, cookies and pastries.</p>
      <p class="person-name">Mara Linden</p>
      <p class="contact">084-5172-0493<br>info@zippypompombakes.com</p>
    </div>
    <div class="pattern-strip pattern-strip--right" role="img" aria-label="White bakery icon pattern of cupcakes, cakes, donuts and pastries on mint green"></div>
  </section>

  <section class="card card--back">
    <div class="pattern-band pattern-band--top" role="img" aria-label="Pink bakery icon pattern of cupcakes, cookies, bread and donuts on white"></div>
    <div class="back-band">
      <div class="back-brand">
        <h2 class="brand-name">Zippy Pom-Pom Bakes</h2>
        <p class="tagline">cakes, muffins, cookies and pastries.</p>
      </div>
      <div class="brand-dot"></div>
    </div>
    <div class="pattern-band pattern-band--bottom" role="img" aria-label="Pink bakery icon pattern of cupcakes, cookies, bread and donuts on white"></div>
  </section>

</main>
</body>
</html>
```